Design for a 3-4 screens mobile app

The app is a "simple" ordering mobile app.
1. START screen : user can select either "NEW order" either "VIEW history" - or, can access the usual Contact, About, and Conditions pages.
2. NEW order : is a sequence of 3 basic screens/forms made of 3-4 fields each. Logic is the following: you select the service you need, its recurrence, mention where you are located and then you post it towards the marketplace...
3. VIEW history : is where you land at the end of the ordering process - and accessible from START screen. You see there your previous orders, and their statuses.
Mandatory : we need design for START screen, NEW order and VIEW history screens.
Design but be optimized for Smartphones, used in Portrait mode.
Please take into account the design of the website promoting the Mobile App: https://tidyvanlane.be/
Optional but of course nice to have if you could propose some design or guidance for Contact, About, and Conditions pages...
Here attached a full screen sequence.
Updates
Thanks for all your proposals ! They were submitted to the final customer, he selects one ASAP !
Number of Pages Required
3 page
Look and feel
Each slider illustrates characteristics of the customer's brand and the style your logo design should communicate.

```html
<!DOCTYPE html>
<html lang="en">
<head>
<meta charset="utf-8">
<title>Tidy Van Lane – App Screens</title>
<link href="https://fonts.googleapis.com/css2?family=Montserrat:wght@500;600&family=Source+Sans+3:wght@400;500&display=swap" rel="stylesheet">
<style>
:root{
  --bg:#1bbc8f;
  --orange:#ff6a00;
  --orange-soft:#f9a23c;
  --yellow:#f5c15a;
  --lime:#a8eb5f;
  --teal:#0db38f;
  --ink:#333333;
  --muted:#6d6d6d;
  --chip:#e9e9e9;
  --cream:#fcf7f4;
  --dark:#3a3a3a;
  --white:#ffffff;
}
*{box-sizing:border-box;margin:0;padding:0}
html,body{width:1200px;height:1200px;overflow:hidden;background:var(--bg)}
body{position:relative;font-family:"Source Sans 3",Arial,sans-serif;color:var(--ink)}
.screen{position:absolute;top:224px;width:413px;height:735px;background:var(--white);overflow:hidden}
.screen--home{left:135px}
.screen--request{left:653px}
.status{position:absolute;top:0;left:0;right:0;height:26px;display:flex;align-items:center;justify-content:space-between;padding:0 7px;font-size:13px;font-family:"Source Sans 3",Arial,sans-serif}
.status .dots{letter-spacing:-1px;font-size:11px;margin-right:3px}
.status .left,.status .right{display:flex;align-items:center;gap:3px}
.status .time{position:absolute;left:0;right:0;text-align:center;pointer-events:none}
.battery{width:26px;height:11px;border:1px solid currentColor;border-radius:2px;padding:1px;position:relative}
.battery::before{content:"";display:block;width:100%;height:100%;background:currentColor}
.battery::after{content:"";position:absolute;right:-3px;top:3px;width:2px;height:4px;background:currentColor}
.appbar{position:absolute;top:26px;left:0;right:0;height:46px;display:flex;align-items:center;justify-content:center;font-family:"Montserrat",sans-serif;font-weight:500;font-size:18px}
.screen--home .appbar{color:var(--orange)}
.menu-dots{position:absolute;right:12px;top:17px;display:flex;gap:4px}
.menu-dots span{width:8px;height:8px;border:1.5px solid var(--ink);border-radius:50%}
.welcome{position:absolute;top:72px;left:0;right:0;height:126px;background:var(--cream);padding:12px 22px}
.welcome h2{font-family:"Montserrat",sans-serif;font-weight:500;font-size:17px;margin-bottom:9px}
.welcome p{font-size:14.4px;line-height:20px;color:var(--muted)}
.tile{position:absolute;left:0;right:0;display:flex;align-items:center;justify-content:center}
.tile--new{top:198px;height:269px;background:linear-gradient(135deg,var(--yellow) 0%,var(--orange-soft) 40%,var(--orange) 100%)}
.tile--history{top:467px;height:268px;background:linear-gradient(135deg,var(--lime) 0%,#4fcf7a 50%,var(--teal) 100%)}
.screen--request .status{color:var(--white);background:transparent}
.request-head{position:absolute;top:0;left:0;right:0;height:72px;background:linear-gradient(180deg,var(--orange) 0%,#fb8a24 60%,#f7b54a 100%)}
.screen--request .appbar{color:var(--white)}
.back{position:absolute;left:12px;top:15px}
.stepbar{position:absolute;top:72px;left:0;right:0;height:44px;background:var(--cream);display:flex;align-items:center;justify-content:center;font-size:15px;color:var(--ink)}
.label{position:absolute;left:22px;font-family:"Montserrat",sans-serif;font-weight:500;font-size:19px;color:var(--ink)}
.chip{position:absolute;height:44px;display:flex;align-items:center;gap:8px;padding:0 12px;background:var(--chip);color:var(--ink);font-size:16.5px;font-weight:500}
.chip--on{background:var(--orange);color:var(--white)}
.chip svg{flex:none}
.hours{position:absolute;left:22px;top:397px;width:121px;height:49px;border:1.5px solid var(--ink);border-radius:3px;display:flex;align-items:center;padding-left:22px;gap:18px;font-family:"Montserrat",sans-serif;font-size:20px}
.hours .num{color:var(--orange)}
.stepper{position:absolute;left:154px;top:397px;width:99px;height:49px;border:1.5px solid var(--orange);border-radius:3px;display:flex}
.stepper span{flex:1;display:flex;align-items:center;justify-content:center}
.stepper span+span{border-left:1.5px solid var(--orange)}
.next{position:absolute;left:22px;top:645px;width:369px;height:65px;background:var(--dark);color:var(--white);border-radius:3px;display:flex;align-items:center;justify-content:center;font-family:"Montserrat",sans-serif;font-weight:500;font-size:19px;letter-spacing:1px}
</style>
</head>
<body>

<section class="screen screen--home">
  <div class="status">
    <div class="left"><span class="dots">●●●●●</span><span>Carrier</span>
      <svg width="14" height="10" viewBox="0 0 14 10"><path d="M1 3.5a8.5 8.5 0 0 1 12 0M3 5.7a5.5 5.5 0 0 1 8 0M5 7.8a2.5 2.5 0 0 1 4 0" fill="none" stroke="currentColor" stroke-width="1.4"/></svg></div>
    <span class="time">9:41 AM</span>
    <div class="right"><span>100%</span><span class="battery"></span></div>
  </div>
  <header class="appbar">TIDY VAN LANE
    <div class="menu-dots"><span></span><span></span><span></span></div>
  </header>
  <div class="welcome">
    <h2>Welcome</h2>
    <p>Should you have any question about this App or our services, do not hesitate to Call us on +32 470 55 21 09 or send email to info@tidyvanlane.be</p>
  </div>
  <a class="tile tile--new" aria-label="New order">
    <svg width="112" height="112" viewBox="0 0 112 112"><circle cx="56" cy="56" r="53" fill="none" stroke="#fff" stroke-width="4"/><path d="M56 34v44M34 56h44" stroke="#fff" stroke-width="4.5"/></svg>
  </a>
  <a class="tile tile--history" aria-label="View history">
    <svg width="112" height="100" viewBox="0 0 112 100" fill="none" stroke="#fff" stroke-width="4.5">
      <path d="M2 20l10 10 18-22"/>
      <path d="M42 16h68M42 24h68M42 51h68M42 59h68M42 87h68M42 95h68" stroke-width="3.5"/>
      <circle cx="17" cy="55" r="9"/><circle cx="17" cy="91" r="9"/>
    </svg>
  </a>
</section>

<section class="screen screen--request">
  <div class="request-head"></div>
  <div class="status">
    <div class="left"><span class="dots">●●●●●</span><span>Carrier</span>
      <svg width="14" height="10" viewBox="0 0 14 10"><path d="M1 3.5a8.5 8.5 0 0 1 12 0M3 5.7a5.5 5.5 0 0 1 8 0M5 7.8a2.5 2.5 0 0 1 4 0" fill="none" stroke="currentColor" stroke-width="1.4"/></svg></div>
    <span class="time">9:41 AM</span>
    <div class="right"><span>100%</span><span class="battery"></span></div>
  </div>
  <header class="appbar">
    <svg class="back" width="30" height="18" viewBox="0 0 30 18" fill="none" stroke="#fff" stroke-width="2.5"><path d="M29 9H3M10 1L2 9l8 8"/></svg>
    SERVICE REQUEST
  </header>
  <div class="stepbar">Step 1 of 4</div>

  <div class="label" style="top:138px">I need</div>
  <div class="chip chip--on" style="left:22px;top:175px;width:121px">
    <svg width="36" height="24" viewBox="0 0 36 24" fill="none" stroke="#fff" stroke-width="1.5"><path d="M2 20h32L30 8H14C8 8 4 13 2 20zM14 8l4-5h14"/></svg>Ironing</div>
  <div class="chip" style="left:154px;top:175px;width:132px">
    <svg width="34" height="32" viewBox="0 0 34 32" fill="none" stroke="#444" stroke-width="1.5"><circle cx="13" cy="18" r="8"/><circle cx="13" cy="18" r="3"/><path d="M4 28h18M24 30V4h4v26M22 30h8"/></svg>Cleaning</div>
  <div class="chip" style="left:22px;top:230px;width:144px">
    <svg width="30" height="34" viewBox="0 0 30 34" fill="none" stroke="#444" stroke-width="1.5"><circle cx="10" cy="8" r="4"/><circle cx="20" cy="8" r="4"/><circle cx="15" cy="4" r="3"/><path d="M15 12v8M6 20h18l-3 12H9z"/></svg>Gardening</div>
  <div class="chip chip--on" style="left:176px;top:230px;width:132px">
    <svg width="26" height="32" viewBox="0 0 26 32" fill="none" stroke="#fff" stroke-width="1.5"><rect x="1" y="1" width="24" height="30" rx="2"/><path d="M1 7h24"/><circle cx="13" cy="19" r="8"/><circle cx="13" cy="19" r="5"/></svg>Laundry</div>
  <div class="chip" style="left:22px;top:286px;width:144px">
    <svg width="32" height="34" viewBox="0 0 32 34" fill="none" stroke="#444" stroke-width="1.5"><path d="M6 2h6v14h16v6H6zM26 14v10M9 24v4"/><circle cx="9" cy="31" r="1.5"/></svg>Plumbing</div>

  <div class="label" style="top:364px">For</div>
  <div class="hours"><span class="num">4</span><span>Hours</span></div>
  <div class="stepper">
    <span><svg width="22" height="4"><path d="M0 2h22" stroke="#ff6a00" stroke-width="3"/></svg></span>
    <span><svg width="24" height="24"><path d="M12 0v24M0 12h24" stroke="#ff6a00" stroke-width="3"/></svg></span>
  </div>

  <div class="label" style="top:474px">Frequency</div>
  <div class="chip chip--on" style="left:22px;top:507px;width:103px;justify-content:center">Only Once</div>
  <div class="chip" style="left:135px;top:507px;width:122px;justify-content:center">Weekly Basis</div>
  <div class="chip" style="left:268px;top:507px;width:110px;justify-content:center">Set Specific</div>

  <div class="next">NEXT STEP</div>
</section>

</body>
</html>
```